Vale Crest Motors Business Card

Would like a cutting edge / high end Automotive Business card design. Please see current card which is old and dated. Would like to maintain the Vale Crest Motors logo and same information (address, website, etc).

See our website for the look and feel of what we offer - www.valecrestmotors.example

Target Market(s)

Upper class car buyers

Contact Information for Business Card

Modern high end business card design

Requirements
Nice to have
• Carbon Fiber look background

```html
<!DOCTYPE html>
<html lang="en">
<head>
<meta charset="utf-8">
<title>Vale Crest Motors Business Card</title>
<link rel="stylesheet" href="https://fonts.googleapis.com/css2?family=Arimo:wght@400&family=Libre+Baskerville:ital,wght@0,400;0,700;1,700&display=swap">
<style>
  :root {
    --backdrop: #0b0b0c;
    --card: #242527;
    --card-edge: #c9b25e;
    --gold: #c6a85a;
    --white: #f2f2f2;
    --rule: #5a5a5c;
    --emboss: #3a3b3e;
  }
  * { box-sizing: border-box; margin: 0; padding: 0; }
  html, body { width: 1200px; height: 820px; overflow: hidden; }
  body {
    background: var(--backdrop);
    font-family: "Arimo", Arial, sans-serif;
    color: var(--white);
    position: relative;
  }
  .card {
    position: absolute;
    top: 255px;
    width: 540px;
    height: 309px;
    background: var(--card);
    border-left: 2px solid var(--card-edge);
    border-bottom: 2px solid var(--card-edge);
    box-shadow: 0 18px 40px rgba(0,0,0,.6);
  }
  .card--front { left: 40px; }
  .card--back { left: 620px; }

  /* Front */
  .brand {
    position: absolute;
    right: 48px;
    top: 58px;
    text-align: right;
  }
  .brand__name {
    font-family: "Libre Baskerville", Georgia, serif;
    font-weight: 400;
    font-size: 30px;
    letter-spacing: .5px;
    color: var(--gold);
    padding-bottom: 8px;
    border-bottom: 1px solid var(--gold);
  }
  .person {
    position: absolute;
    left: 44px;
    top: 150px;
  }
  .person__name {
    font-family: "Libre Baskerville", Georgia, serif;
    font-weight: 700;
    font-size: 22px;
    line-height: 28px;
    color: var(--gold);
    letter-spacing: .5px;
  }
  .person__role {
    font-size: 12px;
    line-height: 16px;
    letter-spacing: .5px;
    margin-top: 2px;
  }
  .divider {
    position: absolute;
    left: 108px;
    right: 48px;
    top: 187px;
    height: 1px;
    background: var(--rule);
  }
  .contacts {
    position: absolute;
    left: 56px;
    top: 210px;
    list-style: none;
    font-size: 13px;
    line-height: 19px;
  }
  .contacts li { display: flex; align-items: center; gap: 8px; }
  .contacts svg { width: 12px; height: 12px; flex: none; }
  .address {
    position: absolute;
    right: 40px;
    top: 204px;
    text-align: right;
    font-size: 13px;
    line-height: 18px;
    font-style: normal;
  }

  /* Back */
  .back__brand {
    position: absolute;
    left: 0; right: 0;
    top: 70px;
    text-align: center;
  }
  .back__brand .brand__name {
    display: inline-block;
    color: var(--emboss);
    border-bottom-color: var(--emboss);
    font-size: 32px;
  }
  .tagline {
    position: absolute;
    left: 0; right: 0;
    top: 150px;
    text-align: center;
    font-family: "Libre Baskerville", Georgia, serif;
    font-style: italic;
    font-weight: 700;
    font-size: 14px;
    line-height: 20px;
  }
  .values {
    position: absolute;
    left: 0; right: 0;
    top: 218px;
    display: flex;
    justify-content: center;
    align-items: center;
    gap: 10px;
    font-size: 12px;
    letter-spacing: .3px;
  }
  .values__dot {
    width: 6px; height: 6px;
    border-radius: 50%;
    background: var(--gold);
  }
</style>
</head>
<body>

<section class="card card--front" aria-label="Card front">
  <div class="brand"><div class="brand__name">Vale Crest Motors</div></div>
  <div class="person">
    <div class="person__name">DANA MERROW</div>
    <div class="person__role">OWNER</div>
  </div>
  <div class="divider"></div>
  <ul class="contacts">
    <li>
      <svg viewBox="0 0 12 12" aria-hidden="true"><path d="M2.5 1l2 2-1 1.3c.6 1.4 1.8 2.6 3.2 3.2l1.3-1 2 2-1.2 1.5C5.5 9.8 2.2 6.5 1 3.2z" fill="var(--gold)"/></svg>
      415.555.0142
    </li>
    <li>
      <svg viewBox="0 0 12 12" aria-hidden="true"><rect x="3" y="1" width="6" height="3" fill="var(--gold)"/><rect x="1" y="4.5" width="10" height="4.5" rx="1" fill="var(--gold)"/><rect x="3" y="7.5" width="6" height="3.5" fill="var(--gold)" stroke="var(--card)" stroke-width=".8"/></svg>
      415.555.0187
    </li>
    <li>
      <svg viewBox="0 0 12 12" aria-hidden="true"><rect x="1" y="2.5" width="10" height="7" fill="var(--gold)"/><path d="M1 2.5l5 4 5-4" fill="none" stroke="var(--card)" stroke-width="1"/></svg>
      dana@valecrestmotors.example
    </li>
    <li>
      <svg viewBox="0 0 12 12" aria-hidden="true"><circle cx="6" cy="6" r="5" fill="none" stroke="var(--gold)" stroke-width="1.2"/><ellipse cx="6" cy="6" rx="2.2" ry="5" fill="none" stroke="var(--gold)"/><path d="M1 6h10M2 3.5h8M2 8.5h8" stroke="var(--gold)" stroke-width=".8"/></svg>
      www.valecrestmotors.example
    </li>
  </ul>
  <address class="address">
    1180 Harbor Ridge Rd #A<br>Linwood, CA 94000
  </address>
</section>

<section class="card card--back" aria-label="Card back">
  <div class="back__brand"><div class="brand__name">Vale Crest Motors</div></div>
  <p class="tagline">Offering the Finest in Luxury<br>and Exotic Cars</p>
  <div class="values">
    <span>QUALITY</span><span class="values__dot"></span>
    <span>INTEGRITY</span><span class="values__dot"></span>
    <span>SERVICE</span>
  </div>
</section>

</body>
</html>
```